Flyer-Design für traditionelles Dorffest
Zielgruppe
Benötigen Flyer/Plakat design A4 Doppelseite für traditionelles Dorffest.
Aufgabenstellung
Das Design soll einem traditionellen Dorffest der Schützenkompanie entsprechen. (Farben: Dunkelgrün oder Rot / Weiß)
Text Vorderseite:
- Die Schützenkompanie Obermoosbach lädt zum Obermoosbacher Dorffest. (Überschrift Obermoosbacher Dorffest groß)
- Samstag 10. August 2019
- Erstmals mit 'Riesen-Fußball-Dart' Turnier ab 14 Uhr
- 17 Uhr Einmarsch der Musikkapelle Obermoosbach mit anschließendem Konzert im Festzelt
- Stimmungsabend mit 'Die fesch'n Gamsler'
- zugestellt durch briefweg.at an einen Haushalt (Kleiner Hinweiß rechts oben)
- Eintritt: 5€ (Kleiner Schriftzug)
- Mit Schießbude, Wein- und Kaffeebar, Weißbierbar, Schützenbar und großer Tombola
Logos Vorderseite:
- Logo Musik 'Die fesch'n Gamsler'.
- Tiroler Adler (Schützen) Eventuell im Hintergrund oder Modifizieren
- Eventuell Bild von Hinterthiersee mit einbauchen (Hintergrund)
Text Hinterseite:
- Überschrift groß: 'Riesen-Fußball-Dart' Turnier
- Beginn um 14 Uhr
- 3 Spieler pro Team
- Startgebühr: 30 € pro Team (Damen, Herren oder Mixed Teams möglich) / Kinderteams 15 €
- Für Unfälle jeglicher Art wird vom Veranstalter keine Haftung übernommen! (Kleine Schrift)
- Wir achten auf den Jugendschutz! (Kleine Schrift)
- Überschrift groß: 'Heimfahrservice innerhalb von Moosbachtal'
Auf Euer Kommen freut sich die Schützenkompanie Obermoosbach!
Logos Rückseite Sponsoren: Kornkasse Bergtal, Laufwerker Obermoosbach, Jausenstation Brunnalm, Loidlmayr Bau, Metzgerei Stangl, Zitherbau Egger, varolin GmbH, Sanitär Technik Aubing
Logos im Anhang. Foto von Hinterthiersee und Tiroler Adler bei Bedarf via Mail (Da nicht mehr Anhänge möglich sind).
Bei Fragen freue Ich mich über Ihre Nachricht.
Vielen Dank für die Vorschläge.

```html
<!DOCTYPE html>
<html lang="de">
<head>
<meta charset="utf-8">
<title>Obermoosbacher Dorffest – Flyer</title>
<link href="https://fonts.googleapis.com/css2?family=Luckiest+Guy&family=Passion+One:wght@400;700&family=Roboto:wght@400;500;700&display=swap" rel="stylesheet">
<style>
  :root {
    --green: #2f8b45;
    --green-dark: #1f6a33;
    --green-light: #3fa357;
    --red: #c0262b;
    --red-dark: #9e1d22;
    --navy: #15283a;
    --white: #ffffff;
    --ink: #222222;
    --page-bg: #e4e4e4;
  }
  * { box-sizing: border-box; margin: 0; padding: 0; }
  html, body { width: 1200px; height: 810px; overflow: hidden; }
  body {
    background: var(--page-bg);
    font-family: "Roboto", Arial, sans-serif;
    color: var(--white);
    position: relative;
  }
  .sheet {
    position: absolute;
    top: 23px;
    width: 540px;
    height: 764px;
    display: flex;
    flex-direction: column;
    overflow: hidden;
    box-shadow: 0 4px 14px rgba(0,0,0,.18);
  }
  .sheet--back { left: 40px; }
  .sheet--front { left: 620px; }

  /* shared */
  .sponsor-bar {
    background: var(--white);
    display: flex;
    align-items: center;
    justify-content: space-around;
    padding: 0 20px;
    color: var(--ink);
  }
  .sponsor {
    display: flex;
    align-items: center;
    gap: 7px;
    font-weight: 700;
    font-size: 14px;
    color: var(--ink);
    line-height: 1.1;
  }
  .sponsor__dot { width: 16px; height: 16px; border-radius: 50%; background: var(--green); flex: none; }
  .sponsor__square { width: 16px; height: 16px; background: var(--red); flex: none; }

  /* back side */
  .sheet--back .sponsor-bar--top { height: 118px; }
  .back-body {
    flex: 1;
    background: radial-gradient(circle at 50% 40%, var(--green-light) 0%, var(--green) 45%, var(--green-dark) 100%);
    display: flex;
    flex-direction: column;
    align-items: center;
    text-align: center;
    padding: 26px 34px 22px;
  }
  .back-title {
    font-family: "Luckiest Guy", "Arial Black", sans-serif;
    font-size: 40px;
    line-height: 1.05;
    letter-spacing: 1px;
  }
  .dart-art {
    margin: 18px 0 18px;
    width: 210px;
    height: 210px;
    border-radius: 50%;
    background: radial-gradient(circle, #e24a3a 0%, var(--red) 55%, var(--red-dark) 100%);
  }
  .back-facts { font-size: 15px; line-height: 1.45; }
  .back-facts strong { font-size: 18px; }
  .back-note { font-size: 10.5px; margin-top: 8px; opacity: .9; line-height: 1.4; }
  .back-service {
    font-family: "Roboto", Arial, sans-serif;
    font-weight: 700;
    font-size: 26px;
    margin-top: 16px;
  }
  .back-closing { font-size: 14px; margin-top: 6px; }
  .sheet--back .sponsor-bar--bottom { height: 120px; flex-wrap: wrap; gap: 6px 10px; }

  /* front side */
  .front-header {
    background: var(--white);
    height: 92px;
    position: relative;
    display: flex;
    align-items: center;
    justify-content: center;
    color: var(--ink);
  }
  .band-name {
    font-family: "Passion One", "Arial Black", sans-serif;
    font-size: 24px;
    color: var(--ink);
    display: flex;
    align-items: center;
    gap: 8px;
  }
  .band-name__dot { width: 14px; height: 14px; border-radius: 50%; background: var(--green); }
  .delivery-note {
    position: absolute;
    right: 18px;
    top: 18px;
    font-size: 10px;
    line-height: 1.35;
    text-align: right;
    color: var(--ink);
  }
  .delivery-note b { font-weight: 700; }
  .front-hero {
    height: 318px;
    position: relative;
    background: radial-gradient(circle at 50% 60%, var(--green-light) 0%, var(--green) 50%, var(--green-dark) 100%);
    text-align: center;
  }
  .front-invite { font-size: 13.5px; padding-top: 36px; }
  .front-title {
    font-family: "Passion One", "Arial Black", sans-serif;
    font-weight: 700;
    font-size: 54px;
    line-height: .98;
    margin-top: 10px;
    letter-spacing: .5px;
  }
  .date-stamp {
    position: absolute;
    left: 40px;
    top: 190px;
    width: 104px;
    border: 3px dashed var(--white);
    transform: rotate(-9deg);
    padding: 6px 4px;
    font-family: "Passion One", "Arial Black", sans-serif;
    line-height: 1;
    text-align: center;
  }
  .date-stamp__day { font-size: 19px; }
  .date-stamp__date { font-size: 32px; color: var(--navy); }
  .date-stamp__year { font-size: 32px; }
  .music-art {
    position: absolute;
    left: 200px;
    top: 170px;
    width: 130px;
    height: 148px;
    border-radius: 50% 50% 40% 40%;
    background: linear-gradient(180deg, rgba(255,255,255,.28), rgba(255,255,255,.08));
  }
  .entry {
    position: absolute;
    right: 30px;
    top: 230px;
    text-align: right;
  }
  .entry__label { font-weight: 700; font-size: 15px; display: flex; align-items: center; gap: 6px; justify-content: flex-end; }
  .entry__price {
    width: 36px; height: 36px; border-radius: 50%;
    background: var(--red); color: var(--white);
    display: inline-flex; align-items: center; justify-content: center;
    font-family: "Passion One", sans-serif; font-size: 22px;
  }
  .entry__hint { font-size: 10px; margin-top: 6px; opacity: .9; }
  .programme {
    background: var(--red);
    padding: 18px 22px 16px;
  }
  .programme__title {
    text-align: center;
    font-size: 14px;
    letter-spacing: .5px;
    margin-bottom: 20px;
  }
  .programme__title span { border-bottom: 1.5px solid var(--white); padding: 0 24px 3px; }
  .programme__row { display: flex; gap: 10px; align-items: flex-start; margin-bottom: 14px; }
  .programme__time {
    font-family: "Roboto", sans-serif; font-weight: 700; font-size: 22px; white-space: nowrap;
  }
  .programme__time small { font-size: 12px; }
  .programme__text { font-size: 11px; line-height: 1.35; padding-top: 5px; }
  .programme__text b { font-size: 13px; }
  .programme__extras { text-align: center; font-size: 11px; margin-top: 6px; }
  .front-footer { flex: 1; background: var(--navy); }
</style>
</head>
<body>

  <section class="sheet sheet--back" aria-label="Rückseite">
    <div class="sponsor-bar sponsor-bar--top">
      <div class="sponsor"><span class="sponsor__square"></span>Kornkasse<br>Bergtal</div>
      <div class="sponsor">Laufwerker<br>Obermoosbach</div>
      <div class="sponsor"><span class="sponsor__dot"></span>Jausenstation<br>Brunnalm</div>
    </div>
    <div class="back-body">
      <h2 class="back-title">Riesen-Fussball-Dart<br>Turnier</h2>
      <div class="dart-art" role="img" aria-label="Illustration einer Fußball-Dartscheibe in Rot"></div>
      <p class="back-facts"><strong>Beginn um 14 Uhr · 3 Spieler pro Team</strong><br>
        Startgebühr: 30 € pro Team (Damen, Herren oder Mixed Teams möglich)<br>
        Kinderteams 15 €</p>
      <p class="back-note">Für Unfälle jeglicher Art wird vom Veranstalter keine Haftung übernommen!<br>
        Wir achten auf den Jugendschutz!</p>
      <p class="back-service">Heimfahrservice innerhalb von Moosbachtal</p>
      <p class="back-closing">Auf Euer Kommen freut sich die Schützenkompanie Obermoosbach!</p>
    </div>
    <div class="sponsor-bar sponsor-bar--bottom">
      <div class="sponsor"><span class="sponsor__square"></span>Loidlmayr Bau</div>
      <div class="sponsor"><span class="sponsor__dot"></span>Metzgerei Stangl</div>
      <div class="sponsor"><span class="sponsor__dot"></span>varolin GmbH</div>
      <div class="sponsor"><span class="sponsor__square"></span>Sanitär Technik Aubing</div>
    </div>
  </section>

  <section class="sheet sheet--front" aria-label="Vorderseite">
    <header class="front-header">
      <div class="band-name"><span class="band-name__dot"></span>Die fesch'n Gamsler</div>
      <p class="delivery-note">zugestellt durch<br><b>briefweg.at</b><br>an einen Haushalt</p>
    </header>
    <div class="front-hero">
      <p class="front-invite">Die Schützenkompanie Obermoosbach lädt zum</p>
      <h1 class="front-title">OBERMOOSBACHER<br>DORFFEST</h1>
      <div class="date-stamp">
        <div class="date-stamp__day">SAMSTAG</div>
        <div class="date-stamp__date">10.08</div>
        <div class="date-stamp__year">2019</div>
      </div>
      <div class="music-art" role="img" aria-label="Illustration eines Notenschlüssels mit geschwungenem Notenband"></div>
      <div class="entry">
        <div class="entry__label">Eintritt: <span class="entry__price">5€</span></div>
        <div class="entry__hint">(Kleiner Schriftzug)</div>
      </div>
    </div>
    <div class="programme">
      <p class="programme__title"><span>PROGRAMM</span></p>
      <div class="programme__row">
        <span class="programme__time">14:00 <small>UHR</small></span>
        <span class="programme__text">Erstmals mit <b>'Riesen-Fußball-Dart'</b> Turnier</span>
      </div>
      <div class="programme__row">
        <span class="programme__time">17:00 <small>UHR</small></span>
        <span class="programme__text">Einmarsch der Musikkapelle Obermoosbach mit anschließendem Konzert im Festzelt Stimmungsabend mit <b>'Die fesch'n Gamsler'</b><br>
          Stimmungsabend mit <b>'Die fesch'n Gamsler'</b></span>
      </div>
      <p class="programme__extras">Mit Schießbude, Wein- und Kaffeebar, Weißbierbar, Schützenbar und großer Tombola</p>
    </div>
    <div class="front-footer"></div>
  </section>

</body>
</html>
```